I want a business letter head designed, one that I can have printed but also one that I can use as an insert for proforma documentation that is printed in house.

Business name : RJ Pemberly & Associates
Address: PO Box 732
Coralbrook Qld 4871

Type of business: Accounting practice- accounting, taxation, audit, self managed superannuation,

Colour scheme: black and blue - previously designed a business card; however the blue that is one the cards is very washed out and I am not particularly happy with it.

```html
<!DOCTYPE html>
<html lang="en">
<head>
<meta charset="utf-8">
<title>RJ Pemberly &amp; Associates – Letterhead</title>
<link rel="stylesheet" href="https://fonts.googleapis.com/css2?family=Arimo:wght@400&display=swap">
<style>
  :root {
    --ink: #000000;
    --paper: #ffffff;
    --brand-blue: #2393bb;
    --rule-grey: #9a9a9a;
  }
  html, body {
    margin: 0;
    padding: 0;
    overflow: hidden;
    background: var(--paper);
  }
  .letterhead {
    position: relative;
    width: 927px;
    height: 1200px;
    overflow: hidden;
    background: var(--paper);
    font-family: "Arimo", Arial, sans-serif;
  }
  .header-band {
    position: absolute;
    left: 0;
    top: 0;
    width: 640px;
    height: 320px;
    background: var(--ink);
    border-bottom-right-radius: 140px;
    box-shadow: 10px 10px 0 0 var(--brand-blue);
  }
  .margin-band {
    position: absolute;
    left: 0;
    top: 320px;
    width: 28px;
    height: 880px;
    background: var(--ink);
    box-shadow: 10px 0 0 0 var(--brand-blue);
  }
  .brand-mark {
    position: absolute;
    left: 104px;
    top: 112px;
    width: 120px;
    height: 120px;
    background: var(--paper);
  }
  .brand-name {
    position: absolute;
    left: 283px;
    top: 134px;
    margin: 0;
    color: var(--paper);
    font-weight: 400;
    font-size: 40px;
    line-height: 40px;
  }
  .brand-address {
    position: absolute;
    left: 240px;
    top: 224px;
    margin: 0;
    color: var(--paper);
    font-size: 22px;
    line-height: 26px;
    font-style: normal;
    white-space: nowrap;
  }
  .header-rule {
    position: absolute;
    left: 71px;
    top: 277px;
    width: 482px;
    height: 1px;
    background: var(--rule-grey);
  }
</style>
</head>
<body>
  <div class="letterhead">
    <div class="header-band"></div>
    <div class="margin-band"></div>
    <div class="brand-mark"></div>
    <h1 class="brand-name">RJ Pemberly<br>&amp; Associates</h1>
    <address class="brand-address">PO Box 732 Coralbrook Qld 4871</address>
    <div class="header-rule"></div>
  </div>
</body>
</html>
```